PRVKA Membership Flyer

• 1 Page Flyer promoting PRVKA Membership Drive
• I have attached our organization brochure for organizational info
• Please include the same PRVKA logo as seen in brochure
• Membership $20/year
• Contact Tomas Weller to Join at wellto42@learners.brvx.edu
INCLUDE Organization Advisers
Dr. Rostam Velani NPV School of Dental Medicine (photo from attached brochure)
Dr. Felix Oyo NPV Tarrow School of Medicine (Photo from Attached brochure)

Member Benefits
• Access to exclusive Interdisciplinary world-renowned guest speaker presentations
• Mentorship for residencies / Oral Medicine Fellowship for nondental healthcare students
• Shadowing opportunities with Oral Medicine Specialist
• Participate in research journal club
• Clinical Research, Case Reports and Lindqvar Fellowship opportunities
• Exclusive Lunch and Learn Invitations
• 10% Discount to Special Events Sponsored by PRVKA
• Enhance your Interdisciplinary resource network

Renew or Join PRVKA by August 30th and be entered in a free raffle for the chance to win one of 3 drawings
$50 Zorel Gift Card
2x $25 Plumfield Gift Card

Target Market(s)

Students

Requirements
Must have
• Must use the PRVKA Logo from brochure, Member Benefits • Access to exclusive Interdisciplinary world-renowned guest speaker presentations • Mentorship for residencies / Oral Medicine Fellowship for nondental healthcare students • Shadowing opportunities with Oral Medicine Specialist • Participate in research journal club • Clinical Research, Case Reports and Lindqvar Fellowship opportunities • Exclusive Lunch and Learn Invitations • 10% Discount to Special Events Sponsored by PRVKA • Enhance your Interdisciplinary resource network Renew or Join PRVKA by August 30th and be entered in a free raffle for the chance to win one of 3-4 drawings $50 Zorel Gift Card 2x $25 Plumfield Gift Card
Nice to have
• Similar design background to brochure attached,

```html
<!DOCTYPE html>
<html lang="en">
<head>
<meta charset="utf-8">
<title>PRVKA Membership Drive</title>
<link href="https://fonts.googleapis.com/css2?family=Libre+Baskerville:wght@700&family=Montserrat:wght@400;500;600;700;800&display=swap" rel="stylesheet">
<style>
:root{
  --purple:#663a93;
  --purple-deep:#55307f;
  --gold:#c9b062;
  --gold-text:#b39a48;
  --ink:#2a2233;
  --muted:#4a4452;
  --white:#ffffff;
  --page:#ffffff;
  --teal-deep:#7fcad4;
  --teal:#a8dde4;
  --teal-soft:#d6eff2;
}
*{margin:0;padding:0;box-sizing:border-box}
html,body{width:783px;height:1200px;overflow:hidden;background:var(--page)}
body{font-family:"Montserrat",Arial,sans-serif;color:var(--ink)}
.flyer{position:relative;width:783px;height:1200px;overflow:hidden;background:var(--page)}

/* hero */
.hero-photo{position:absolute;left:0;top:0;width:783px;height:540px;
  background:
    radial-gradient(ellipse 260px 300px at 150px 330px,rgba(255,255,255,.55) 0%,rgba(255,255,255,0) 70%),
    radial-gradient(ellipse 220px 200px at 290px 230px,var(--teal-deep) 0%,rgba(127,202,212,0) 75%),
    linear-gradient(90deg,var(--teal) 0%,var(--teal-deep) 22%,var(--teal) 42%,var(--teal-soft) 58%,#f4fbfc 70%,#ffffff 80%);}
.hero-shapes{position:absolute;left:0;top:0}
.brand{position:absolute;left:440px;top:98px;width:300px;text-align:center;color:var(--purple);
  font-family:"Montserrat",Arial,sans-serif;font-weight:700;font-size:40px;line-height:1;letter-spacing:1px}
.drive{position:absolute;left:412px;top:258px;width:371px;text-align:center;color:var(--white)}
.drive-title{font-family:"Libre Baskerville",Georgia,serif;font-weight:700;font-size:74px;line-height:1;letter-spacing:1px}
.drive-sub{font-family:"Libre Baskerville",Georgia,serif;font-weight:700;font-size:24px;color:var(--gold);margin-top:8px;letter-spacing:.5px}
.drive-dash{width:28px;height:4px;border-radius:2px;background:var(--gold);margin:10px 0 0 32px}
.price-pill{position:absolute;left:434px;top:410px;width:287px;height:38px;border-radius:19px;background:var(--gold);overflow:hidden}
.price-pill .label{position:absolute;left:0;top:0;height:38px;width:150px;background:var(--white);
  clip-path:polygon(0 0,100% 0,88% 100%,0 100%);border-radius:19px 0 0 19px;
  display:flex;align-items:center;padding-left:20px;font-weight:600;font-size:16px;color:var(--purple)}
.price-pill .amount{position:absolute;left:160px;top:2px;color:var(--white);font-weight:800;font-size:30px;line-height:34px}
.price-pill .amount sup{font-size:14px;vertical-align:top;position:relative;top:2px}
.price-pill .amount small{font-weight:500;font-size:16px;margin-left:4px}

/* sections */
.section-title{position:absolute;font-weight:600;font-size:19px;letter-spacing:-.2px;color:var(--ink)}
.section-title span{color:var(--purple)}
.section-title::after{content:"";display:block;width:32px;height:2px;background:var(--ink);margin-top:14px}
.benefits-title{left:56px;top:570px}
.advisers-title{left:426px;top:570px}

.benefit-list{position:absolute;left:56px;top:658px;width:285px;list-style:none}
.benefit-list li{position:relative;padding-left:36px;font-size:12.8px;font-weight:500;line-height:16px;margin-bottom:15px;color:var(--ink)}
.benefit-list li svg{position:absolute;left:0;top:1px}

.discount{position:absolute;left:56px;top:1026px;display:flex;align-items:center}
.discount-fig{width:80px}
.discount-fig b{display:block;font-size:36px;font-weight:800;color:var(--gold-text);line-height:1;letter-spacing:-1px}
.discount-fig span{font-size:14px;font-weight:500}
.discount-rule{width:1px;height:58px;border-left:1px dashed #777;margin:0 18px 0 4px}
.discount-text{font-size:15px;font-weight:500;line-height:20px}

/* advisers */
.adviser{position:absolute;left:420px;display:flex;align-items:center}
.adviser-1{top:647px}
.adviser-2{top:776px}
.adviser-ring{position:relative;width:112px;height:112px}
.adviser-photo{position:absolute;left:10px;top:6px;width:100px;height:100px;border-radius:50%;
  border:4px solid #e9e6ee;background:radial-gradient(circle at 50% 40%,#9a8f88 0%,#6e6a6e 55%,#c9ccd2 100%)}
.adviser-info{margin-left:10px}
.adviser-name{font-weight:700;font-size:18.5px;color:var(--ink);letter-spacing:-.3px}
.adviser-school{font-size:14.5px;font-weight:500;color:var(--muted);line-height:18px;margin-top:4px;width:170px}

/* raffle */
.raffle{position:absolute;left:431px;top:898px;width:298px;height:68px;border-radius:7px;overflow:hidden;background:var(--gold)}
.raffle-top{height:46px;display:flex;align-items:center;padding-left:18px;font-size:8.5px;font-weight:600;color:var(--ink)}
.raffle-sep{width:1px;height:20px;border-left:1px dashed var(--ink);margin:0 12px}
.raffle-date{font-size:13px;font-weight:600;color:var(--purple)}
.raffle-date b{color:var(--ink);font-weight:800;font-size:21px;margin-left:4px}
.raffle-date sup{font-size:10px;color:var(--ink);font-weight:700}
.raffle-bottom{height:22px;background:var(--purple);color:var(--white);font-size:7.2px;font-weight:500;display:flex;align-items:center;justify-content:center}

.gift{position:absolute;top:990px;width:141px;height:86px;border-radius:8px;background:var(--white);
  box-shadow:0 2px 6px rgba(0,0,0,.25)}
.gift-1{left:431px}
.gift-2{left:589px}
.gift-ribbon{position:absolute;left:20px;top:2px;width:14px;height:78px;background:linear-gradient(90deg,#7d3fa6,#a75cc9,#7d3fa6)}
.gift-value{position:absolute;left:62px;top:22px;font-weight:800;font-size:29px;color:var(--ink);line-height:1}
.gift-value sup{font-size:15px}
.gift-note{position:absolute;left:62px;top:54px;font-size:7.5px;font-weight:500;color:var(--ink)}
.gift-2 .gift-value{font-size:17px;top:22px;left:70px}
.gift-2 .gift-brand{position:absolute;left:70px;top:43px;font-size:9px;color:#6b6670;line-height:11px}
.gift-2 .gift-brand b{display:block;color:var(--ink);font-weight:500;font-size:10.5px}

/* footer */
.footer-shape{position:absolute;left:0;top:1103px}
.phone{position:absolute;left:56px;top:1133px;display:flex;align-items:center;color:var(--white);font-weight:700;font-size:17px}
.phone svg{margin-right:6px}
.join{position:absolute;left:231px;top:1122px;color:var(--white);font-size:12.5px;font-weight:600}
.join-mail{display:flex;align-items:center;font-weight:500;font-size:14px;margin-top:2px}
.join-mail svg{margin-right:8px}
.web{position:absolute;left:520px;top:1136px;display:flex;align-items:center;font-size:13.5px;color:var(--muted);font-weight:500}
.web svg{margin-right:9px}
</style>
</head>
<body>
<main class="flyer">

  <div class="hero-photo" role="img" aria-label="Photo of a doctor in a white coat with a stethoscope touching a translucent medical interface of teal hexagons"></div>

  <svg class="hero-shapes" width="783" height="540" viewBox="0 0 783 540" aria-hidden="true">
    <path d="M440 198 Q383 202 378 272 L372 420 Q366 515 296 540 L783 540 V198 Z" fill="var(--gold)"/>
    <path d="M446 206 H783 V489 Q610 478 458 492 Q426 528 328 540 H318 Q382 512 386 420 L392 276 Q396 213 446 206 Z" fill="var(--purple)"/>
    <path d="M458 492 Q610 478 783 489 V494 Q610 483 462 497 Z" fill="var(--white)"/>
  </svg>

  <div class="brand">NPV PRVKA</div>

  <div class="drive">
    <div class="drive-title">PRVKA</div>
    <div class="drive-sub">MEMBERSHIP DRIVE</div>
    <div class="drive-dash"></div>
  </div>

  <div class="price-pill">
    <span class="label">MEMBERSHIP</span>
    <span class="amount"><sup>$</sup>20<small>YEAR</small></span>
  </div>

  <h2 class="section-title benefits-title">MEMBER <span>BENEFITS</span></h2>
  <h2 class="section-title advisers-title">ORGANIZATION <span>ADVISERS</span></h2>

  <ul class="benefit-list">
    <li><svg width="17" height="17" viewBox="0 0 17 17"><circle cx="8.5" cy="8.5" r="8.5" fill="var(--purple)"/><path d="M4.8 8.7 7.4 11.2 12.2 6.2" stroke="#fff" stroke-width="1.8" fill="none"/></svg>Access to exclusive Interdisciplinary world-renowned guest speaker presentations</li>
    <li><svg width="17" height="17" viewBox="0 0 17 17"><circle cx="8.5" cy="8.5" r="8.5" fill="var(--purple)"/><path d="M4.8 8.7 7.4 11.2 12.2 6.2" stroke="#fff" stroke-width="1.8" fill="none"/></svg>Mentorship for residencies / Oral Medicine Fellowship for nondental healthcare students</li>
    <li><svg width="17" height="17" viewBox="0 0 17 17"><circle cx="8.5" cy="8.5" r="8.5" fill="var(--purple)"/><path d="M4.8 8.7 7.4 11.2 12.2 6.2" stroke="#fff" stroke-width="1.8" fill="none"/></svg>Shadowing opportunities with Oral Medicine Specialist</li>
    <li><svg width="17" height="17" viewBox="0 0 17 17"><circle cx="8.5" cy="8.5" r="8.5" fill="var(--purple)"/><path d="M4.8 8.7 7.4 11.2 12.2 6.2" stroke="#fff" stroke-width="1.8" fill="none"/></svg>Participate in research journal club</li>
    <li><svg width="17" height="17" viewBox="0 0 17 17"><circle cx="8.5" cy="8.5" r="8.5" fill="var(--purple)"/><path d="M4.8 8.7 7.4 11.2 12.2 6.2" stroke="#fff" stroke-width="1.8" fill="none"/></svg>Clinical Research, Case Reports and Lindqvar Fellowship opportunities</li>
    <li><svg width="17" height="17" viewBox="0 0 17 17"><circle cx="8.5" cy="8.5" r="8.5" fill="var(--purple)"/><path d="M4.8 8.7 7.4 11.2 12.2 6.2" stroke="#fff" stroke-width="1.8" fill="none"/></svg>Exclusive Lunch and Learn Invitations</li>
    <li><svg width="17" height="17" viewBox="0 0 17 17"><circle cx="8.5" cy="8.5" r="8.5" fill="var(--purple)"/><path d="M4.8 8.7 7.4 11.2 12.2 6.2" stroke="#fff" stroke-width="1.8" fill="none"/></svg>Enhance your Interdisciplinary<br>resource network</li>
  </ul>

  <div class="discount">
    <div class="discount-fig"><b>10%</b><span>Discount</span></div>
    <div class="discount-rule"></div>
    <div class="discount-text">To Special Events<br>Sponsored by PRVKA</div>
  </div>

  <div class="adviser adviser-1">
    <div class="adviser-ring">
      <svg width="112" height="112" viewBox="0 0 112 112" aria-hidden="true"><path d="M60 6 A50 50 0 0 0 60 106" fill="none" stroke="var(--purple)" stroke-width="3.5" stroke-dasharray="0.1 7" stroke-linecap="round"/></svg>
      <div class="adviser-photo" role="img" aria-label="Portrait photo of Dr. Rostam Velani"></div>
    </div>
    <div class="adviser-info">
      <div class="adviser-name">DR. ROSTAM VELANI</div>
      <div class="adviser-school">NPV School of Dental Medicine</div>
    </div>
  </div>

  <div class="adviser adviser-2">
    <div class="adviser-ring">
      <svg width="112" height="112" viewBox="0 0 112 112" aria-hidden="true"><path d="M60 6 A50 50 0 0 0 60 106" fill="none" stroke="var(--purple)" stroke-width="3.5" stroke-dasharray="0.1 7" stroke-linecap="round"/></svg>
      <div class="adviser-photo" role="img" aria-label="Portrait photo of Dr. Felix Oyo"></div>
    </div>
    <div class="adviser-info">
      <div class="adviser-name">DR. FELIX OYO</div>
      <div class="adviser-school">NPV Tarrow School of Medicine</div>
    </div>
  </div>

  <div class="raffle">
    <div class="raffle-top">RENEW OR JOIN PRVKA BY<span class="raffle-sep"></span><span class="raffle-date">AUGUST<b>30</b><sup>th</sup></span></div>
    <div class="raffle-bottom">and be entered in a free raffle for the chance to win one of 3 drawings</div>
  </div>

  <div class="gift gift-1">
    <div class="gift-ribbon" role="img" aria-label="Purple gift ribbon"></div>
    <div class="gift-value"><sup>$</sup>50</div>
    <div class="gift-note">ZOREL GIFT CARD</div>
  </div>
  <div class="gift gift-2">
    <div class="gift-ribbon" role="img" aria-label="Purple gift ribbon"></div>
    <div class="gift-value">2X $25</div>
    <div class="gift-brand">PLUMFIELD<b>GIFT CARD</b></div>
  </div>

  <svg class="footer-shape" width="783" height="97" viewBox="0 0 783 97" aria-hidden="true">
    <path d="M520 82 H783 V97 H528 Z" fill="var(--gold)"/>
    <path d="M0 0 H462 Q488 0 498 20 L534 97 H0 Z" fill="var(--purple)"/>
  </svg>

  <div class="phone">
    <svg width="15" height="15" viewBox="0 0 24 24"><path d="M6.6 10.8a15 15 0 0 0 6.6 6.6l2.2-2.2c.3-.3.7-.4 1-.2 1.1.4 2.3.6 3.6.6.6 0 1 .4 1 1V20c0 .6-.4 1-1 1C10.6 21 3 13.4 3 4c0-.6.4-1 1-1h3.5c.6 0 1 .4 1 1 0 1.3.2 2.5.6 3.6.1.3 0 .7-.2 1Z" fill="var(--gold)"/></svg>
    014.555.0192
  </div>

  <div class="join">
    Tomas Weller to Join at
    <div class="join-mail">
      <svg width="12" height="9" viewBox="0 0 12 9"><rect width="12" height="9" fill="var(--gold)"/><path d="M0 0 6 5 12 0" stroke="var(--purple)" fill="none"/></svg>
      wellto42@learners.brvx.edu
    </div>
  </div>

  <div class="web">
    <svg width="16" height="16" viewBox="0 0 16 16" fill="none" stroke="var(--purple)" stroke-width="1.2"><circle cx="8" cy="8" r="7"/><ellipse cx="8" cy="8" rx="3" ry="7"/><path d="M1 8h14M2 4.5h12M2 11.5h12"/></svg>
    wellto42learners.brvx.edu.com
  </div>

</main>
</body>
</html>
```